Darrel K. Holloway, MD

I would like to set up a web page for my new psychiatric practice. It should summarize my credentials and approach to care plus a patient portal to complete forms before appointments.
I am uploading a powerpoint with my contact information along with the color palette and format I would like to use. The email on the slide has not been reserved and I will need to reserve the domain as part of this process.

```html
<!DOCTYPE html>
<html lang="en">
<head>
<meta charset="utf-8">
<title>Darrel K. Holloway, MD – Psychiatric Practitioner</title>
<link rel="stylesheet" href="https://fonts.googleapis.com/css2?family=Exo+2:wght@300;400;500;600;700&display=swap">
<style>
:root{
  --blue:#1a80f0;
  --blue-dark:#0e6ad6;
  --orange:#fdb53c;
  --ink:#2b2b2b;
  --muted:#7a7a7a;
  --light:#f4f4f4;
  --footer:#1c1c1c;
  --footer-text:#d8d8d8;
  --btn:#555555;
  --white:#ffffff;
}
*{margin:0;padding:0;box-sizing:border-box}
html,body{width:1200px;height:2932px;overflow:hidden}
body{position:relative;font-family:"Exo 2",sans-serif;color:var(--ink);background:var(--white)}

/* header */
.site-header{position:absolute;left:0;top:0;width:1200px;height:94px;background:var(--blue);border-bottom:4px solid var(--blue-dark)}
.brand{position:absolute;left:127px;top:26px;color:var(--white);font-weight:700;font-size:30px;letter-spacing:.2px}
.brand small{font-size:14px;font-weight:400;margin-left:4px}
.main-nav{position:absolute;right:130px;top:0;height:90px;display:flex}
.main-nav a{display:flex;align-items:center;padding:0 18px;color:var(--white);font-size:15px;font-weight:600;text-decoration:none}
.main-nav a.active{background:var(--orange);padding:0 17px}

/* hero */
.hero{position:absolute;left:0;top:94px;width:1200px;height:512px;background:linear-gradient(100deg,#2a2a2a 0%,#4b4741 40%,#6d5e4a 62%,#2f2c28 100%)}
.hero-caption{position:absolute;left:125px;top:228px;width:375px;height:209px;background:rgba(0,0,0,.55);padding:14px 22px}
.hero-caption .lead{color:var(--white);font-weight:300;font-size:32px;line-height:1}
.hero-caption .title{font-weight:600;font-size:60px;line-height:1.05;margin-top:2px}
.hero-caption .title .o{color:var(--orange)}
.hero-caption .title .w{color:var(--white)}
.hero-dots{position:absolute;left:562px;top:469px;display:flex;gap:9px}
.hero-dots i{width:10px;height:10px;border-radius:50%;background:var(--white)}
.hero-dots i.on{background:var(--blue)}

/* about */
.about{position:absolute;left:0;top:606px;width:1200px;height:394px;background:var(--orange)}
.about-photo{position:absolute;left:129px;top:70px;width:219px;height:248px;background:var(--white);padding:7px;box-shadow:0 3px 6px rgba(0,0,0,.2)}
.about-photo div{width:100%;height:100%;background:linear-gradient(160deg,#e9eef2,#b8c2cc)}
.about h2{position:absolute;left:397px;top:80px;color:var(--white);font-weight:400;font-size:29px}
.about-text{position:absolute;left:397px;top:140px;width:672px;color:var(--white);font-size:11.5px;line-height:21px}
.about-text p+p{margin-top:12px}

/* section headings */
.sec-head{position:absolute;height:33px;border-bottom:2px solid #e3e3e3}
.sec-head h2{color:var(--blue);font-weight:600;font-size:29px;line-height:1;margin-top:-6px}
.sec-head .arrows{position:absolute;right:0;top:2px;display:flex;gap:7px}

/* service cards */
.svc{position:absolute;width:295px}
.svc .pic{height:160px;border:1px solid #d6d6d6;box-shadow:0 3px 4px rgba(0,0,0,.15)}
.svc h3{margin-top:20px;font-weight:400;font-size:18px;color:#222}
.svc p{margin-top:9px;font-size:11px;line-height:20px;color:var(--muted);height:80px;overflow:hidden}
.btn{display:inline-block;margin-top:18px;width:114px;height:35px;line-height:35px;text-align:center;background:var(--btn);color:var(--white);font-size:13px;border-radius:2px}

/* news */
.news{position:absolute;left:774px;width:297px}
.news .pic{height:149px}
.news .cap{height:80px;background:var(--orange);display:flex;align-items:center;padding:0 10px}
.news .date{flex:none;color:var(--white);font-weight:600;font-size:24px;line-height:25px;padding-right:10px;border-right:1px solid rgba(255,255,255,.7);height:58px;display:flex;flex-direction:column;justify-content:center}
.news .cap p{color:var(--white);font-size:11px;line-height:20px;padding-left:10px;width:195px}

.newsletter{position:absolute;left:774px;top:1634px;width:297px;height:257px;background:var(--blue);padding:20px 14px}
.newsletter .l1{color:var(--orange);font-size:30px;font-weight:400;line-height:1}
.newsletter .l2{color:var(--white);font-size:30px;font-weight:700;line-height:1.1}
.newsletter p{color:var(--white);font-size:11.5px;line-height:20px;margin-top:10px}
.newsletter .field{margin-top:18px;height:35px;background:#5aa6f7}
.newsletter .sub{display:inline-block;margin-top:12px;background:var(--orange);color:var(--white);font-size:12px;font-weight:700;padding:0 10px;height:35px;line-height:35px}

/* testimonials */
.testimonials{position:absolute;left:0;top:1964px;width:1200px;height:469px;background:var(--light);border-bottom:3px solid var(--orange)}
.testimonials h2{position:absolute;left:0;width:1200px;top:60px;text-align:center;color:var(--blue);font-size:29px;font-weight:600}
.t-card{position:absolute;top:136px;width:227px}
.t-tab{position:absolute;left:63px;top:0;width:100px;height:80px;background:var(--orange);border-radius:50px 50px 0 0;text-align:center;color:var(--white);font-size:46px;font-weight:700;line-height:66px}
.t-photo{position:absolute;left:0;top:55px;width:227px;height:219px;background:var(--orange);border-radius:10px;padding:7px}
.t-photo div{width:100%;height:100%;border-radius:6px}
.t-shadow{position:absolute;left:20px;top:286px;width:187px;height:18px;border-radius:50%;background:radial-gradient(ellipse at center,rgba(0,0,0,.18),rgba(0,0,0,0) 70%)}
.notch{position:absolute;left:262px;top:2433px;width:0;height:0;border-left:9px solid transparent;border-right:9px solid transparent;border-top:12px solid var(--orange)}
.quote{position:absolute;left:140px;top:2476px;width:920px;text-align:center;font-size:14.5px;line-height:24px;color:#444}

/* footer */
.site-footer{position:absolute;left:0;top:2618px;width:1200px;height:314px;background:var(--footer)}
.f-col{position:absolute;top:50px}
.f-col h4{color:var(--blue);font-size:13px;font-weight:600;margin-bottom:18px}
.f-col li{list-style:none;color:var(--footer-text);font-size:11.5px;line-height:25px}
.contact-row{display:flex;gap:18px;color:var(--footer-text);font-size:11.5px;line-height:25px}
.contact-row svg{flex:none;margin-top:6px}
.social{display:flex;gap:16px;margin-top:2px}
.social i{width:11px;height:11px;border-radius:50%;background:var(--orange)}
.copy{position:absolute;left:0;width:1200px;top:278px;text-align:center;color:var(--footer-text);font-size:11.5px}
</style>
</head>
<body>

<header class="site-header">
  <div class="brand">Darrel K. Holloway,<small>MD, Inc</small></div>
  <nav class="main-nav">
    <a class="active">Home</a><a>About Us</a><a>Services</a><a>FAQ's</a><a>Testimonials</a><a>Contact Us</a>
  </nav>
</header>

<section class="hero" role="img" aria-label="Photo of a woman sitting by a barred window in a dim brick room">
  <div class="hero-caption">
    <div class="lead">I'm a solo</div>
    <div class="title"><span class="o">Psychiatric</span><br><span class="w">Practitioner</span></div>
  </div>
  <div class="hero-dots"><i class="on"></i><i></i><i></i><i></i></div>
</section>

<section class="about">
  <div class="about-photo"><div role="img" aria-label="Portrait of the doctor in a white coat with stethoscope"></div></div>
  <h2>About Me</h2>
  <div class="about-text">
    <p>Lorem Ipsum is simply dummy text of the printing and typesetting industry. Lorem Ipsum has been the industry's standard dummy text ever since the 1500s, when an unknown printer took a galley of type and scrambled it to make a type specimen book. It has survived not only five centuries, but also the leap into electronic typesetting, remaining essentially unchanged.</p>
    <p>It was popularised in the 1960s with the release of Lettrafix sheets containing Lorem Ipsum passages, and more recently with desktop publishing software like Quillset Composer including versions of Lorem Ipsum. Lorem Ipsum is simply dummy text of the printing and typesetting industry. Lorem Ipsum has been the industry's standard dummy text ever since the 1500s, when an unknown printer took a galley of type and scrambled it to make a type specimen book. It has survived not only five centuries.</p>
  </div>
</section>

<div class="sec-head" style="left:127px;top:1055px;width:621px">
  <h2>Our Services</h2>
  <div class="arrows"><svg width="28" height="14" viewBox="0 0 28 14"><path d="M8 2 3 7l5 5M20 2l5 5-5 5" fill="none" stroke="#222" stroke-width="2"/></svg></div>
</div>
<div class="sec-head" style="left:774px;top:1055px;width:297px">
  <h2>News</h2>
  <div class="arrows"><svg width="28" height="14" viewBox="0 0 28 14"><path d="M8 2 3 7l5 5M20 2l5 5-5 5" fill="none" stroke="#222" stroke-width="2"/></svg></div>
</div>

<article class="svc" style="left:129px;top:1135px">
  <div class="pic" role="img" aria-label="Woman at a laptop holding her head" style="background:linear-gradient(120deg,#e8e8ea,#c9b3a4)"></div>
  <h3>Anxiety Disorders</h3>
  <p>Lorem Ipsum is simply dummy text of the printing and typesetting industry. Lorem Ipsum has been the industry's standard dummy text ever since the 1500s, when an unknown printer took a galley of type and</p>
  <span class="btn">Read More</span>
</article>
<article class="svc" style="left:451px;top:1135px">
  <div class="pic" role="img" aria-label="Child playing with a tablet" style="background:linear-gradient(120deg,#f1c56a,#4a7fb0)"></div>
  <h3>Autism</h3>
  <p>Lorem Ipsum is simply dummy text of the printing and typesetting industry. Lorem Ipsum has been the industry's standard dummy text ever since the 1500s, when an unknown printer took a galley of type and</p>
  <span class="btn">Read More</span>
</article>
<article class="svc" style="left:129px;top:1538px">
  <div class="pic" role="img" aria-label="Man sitting alone by a window" style="background:linear-gradient(120deg,#5c5f66,#c9d0d8)"></div>
  <h3>Personal / Personality</h3>
  <p>Lorem Ipsum is simply dummy text of the printing and typesetting industry. Lorem Ipsum has been the industry's standard dummy text ever since the 1500s, when an unknown printer took a galley of type and</p>
  <span class="btn">Read More</span>
</article>
<article class="svc" style="left:451px;top:1538px">
  <div class="pic" role="img" aria-label="Wooden letter cubes spelling trauma" style="background:linear-gradient(120deg,#c89a62,#8a6238)"></div>
  <h3>Trauma</h3>
  <p>Lorem Ipsum is simply dummy text of the printing and typesetting industry. Lorem Ipsum has been the industry's standard dummy text ever since the 1500s, when an unknown printer took a galley of type and</p>
  <span class="btn">Read More</span>
</article>

<article class="news" style="top:1133px">
  <div class="pic" role="img" aria-label="Young woman sitting against a pale wall" style="background:linear-gradient(120deg,#9fb3c8,#dbe4ee)"></div>
  <div class="cap"><div class="date">DEC<br>2016</div><p>Neque porro quisquam est qui dolorem ipsum quia dolor sit amet, consectetur</p></div>
</article>
<article class="news" style="top:1383px">
  <div class="pic" role="img" aria-label="Two women talking in a counselling session" style="background:linear-gradient(120deg,#5a5f5a,#cfd2cc)"></div>
  <div class="cap"><div class="date">DEC<br>2016</div><p>Neque porro quisquam est qui dolorem ipsum quia dolor sit amet, consectetur</p></div>
</article>

<aside class="newsletter">
  <div class="l1">SIGN UP</div>
  <div class="l2">NEWSLETTER</div>
  <p>Lorem Ipsum is simply dummy text of the printing and typesetting industry.</p>
  <div class="field"></div>
  <span class="sub">SUBSCRIBE NOW</span>
</aside>

<section class="testimonials">
  <h2>Testimonials</h2>
  <div class="t-card" style="left:160px">
    <div class="t-tab">”</div>
    <div class="t-photo"><div role="img" aria-label="Portrait of a smiling client" style="background:linear-gradient(150deg,#7ea35a,#c79a7a)"></div></div>
    <div class="t-shadow"></div>
  </div>
  <div class="t-card" style="left:484px">
    <div class="t-tab">”</div>
    <div class="t-photo"><div role="img" aria-label="Portrait of a client in a suit" style="background:linear-gradient(150deg,#a9bfd4,#3a4454)"></div></div>
    <div class="t-shadow"></div>
  </div>
  <div class="t-card" style="left:807px">
    <div class="t-tab">”</div>
    <div class="t-photo"><div role="img" aria-label="Portrait of a client in a grey shirt" style="background:linear-gradient(150deg,#6d6b68,#b9a08e)"></div></div>
    <div class="t-shadow"></div>
  </div>
</section>
<div class="notch"></div>
<p class="quote">Lorem ipsum dolor sit amet, consectetur adipiscing elit, sed do eiusmod tempor incididunt ut labore et dolore magna aliqua. Ut enim ad minim veniam, quis nostrud exercitation ullamco laboris nisi ut aliquip ex ea commodo consequat. Duis aute irure dolor in reprehenderit in voluptate velit esse cillum dolore eu fugiat nulla pariatur. Excepteur sint occaecat cupidatat non proident, sunt in culpa qui officia deserunt mollit anim id est laborum.</p>

<footer class="site-footer">
  <div class="f-col" style="left:127px">
    <h4>Quick Links</h4>
    <ul><li>Home</li><li>About Us</li><li>Services</li><li>FAQ's</li><li>Testimonials</li><li>Contact Us</li></ul>
  </div>
  <div class="f-col" style="left:369px">
    <h4>Other Links</h4>
    <ul><li>Terms Of Use</li><li>Privacy policy</li></ul>
  </div>
  <div class="f-col" style="left:612px">
    <h4>Contact Us</h4>
    <div class="contact-row">
      <svg width="12" height="12" viewBox="0 0 12 12"><path d="M1 4 6 1l5 3v1H1zM2 6h1.5v4H2zm3.2 0h1.6v4H5.2zM8.5 6H10v4H8.5zM1 10.5h10V12H1z" fill="#fdb53c"/></svg>
      <div>Darrel K. Holloway, MD, MBA<br>PO Box 7420 PMB 311<br>Cedar Grove, CA 90514</div>
    </div>
    <div class="contact-row" style="margin-top:22px">
      <svg width="12" height="12" viewBox="0 0 12 12"><path d="M2.5 1 4.5 3 3.5 4.5c.8 1.7 2 2.9 3.7 3.7L8.7 7.2l2 2L9.5 11C5 10.5 1.5 7 1 2.5z" fill="#fdb53c"/></svg>
      <div>555-210-4478</div>
    </div>
    <div class="contact-row">
      <svg width="12" height="12" viewBox="0 0 12 12"><rect x="1" y="2.5" width="10" height="7" fill="none" stroke="#fdb53c" stroke-width="1.2"/><path d="M1 3l5 4 5-4" fill="none" stroke="#fdb53c" stroke-width="1.2"/></svg>
      <div>darrel@dkhollowaymd.com</div>
    </div>
  </div>
  <div class="f-col" style="left:934px">
    <h4>Connect With Us</h4>
    <div class="social"><i></i><i></i><i></i></div>
  </div>
  <div class="copy">© 2016 Company Name | All Rights Reserved</div>
</footer>

</body>
</html>
```